Fashion Label Startup Business Card Design

Marianne Velk is a startup fashion designer based on the Gold Coast in QLD Australia. Mariannes label " Sorrina by Velk " is based upon taking old world design techniques and infusing them modern twist. The card design should incorporate an old world theme using colours like mustard, ocha, black, white and elements of lace pattern.

Card Details:

Marianne Velk
Fashion Designer
P: 04 0163 5271
E: sorrinabyvelk@mailbrook.net
W: www.threadpage.net/SOrrinaByVelk

```html
<!DOCTYPE html>
<html lang="en">
<head>
<meta charset="utf-8">
<title>Sorrina by Velk — Business Card</title>
<link rel="stylesheet" href="https://fonts.googleapis.com/css2?family=Oranienbaum&display=swap">
<style>
  :root {
    --paper: #ffffff;
    --ink: #111111;
    --card-edge: #000000;
    --ornament-highlight: #efe9cf;
    --ornament-ochre: #c9b27a;
    --ornament-silver: #9c9a94;
    --ornament-shadow: #4d4b47;
  }
  html, body {
    margin: 0;
    padding: 0;
    width: 846px;
    height: 1200px;
    overflow: hidden;
    background: var(--paper);
  }
  .sheet {
    position: relative;
    width: 846px;
    height: 1200px;
    font-family: "Oranienbaum", serif;
    color: var(--ink);
  }
  .card {
    position: absolute;
    left: 165px;
    width: 514px;
    height: 315px;
    box-sizing: border-box;
    border: 2.5px solid var(--card-edge);
    border-radius: 4px;
    background: var(--paper);
    overflow: hidden;
  }
  .card--front { top: 230px; }
  .card--back  { top: 606px; }
  .card__art {
    position: absolute;
    left: 0;
    top: 0;
    width: 509px;
    height: 310px;
  }
  .ornament-stop-highlight { stop-color: var(--ornament-highlight); }
  .ornament-stop-ochre     { stop-color: var(--ornament-ochre); }
  .ornament-stop-silver    { stop-color: var(--ornament-silver); }
  .ornament-stop-shadow    { stop-color: var(--ornament-shadow); }

  .brand-name {
    font-family: "Oranienbaum", serif;
    font-size: 64px;
    fill: var(--ink);
  }
  .contact__title {
    font-family: "Oranienbaum", serif;
    font-size: 27px;
    font-variant: small-caps;
    fill: var(--ink);
  }
  .contact__line {
    font-family: "Oranienbaum", serif;
    font-size: 13px;
    font-variant: small-caps;
    fill: var(--ink);
  }
</style>
</head>
<body>
<main class="sheet">
  <section class="card card--front">
    <svg class="card__art" viewBox="0 0 509 310" xmlns="http://www.w3.org/2000/svg">
      <defs>
        <radialGradient id="ornament-tone" cx="50%" cy="45%" r="60%">
          <stop offset="0%" class="ornament-stop-highlight"/>
          <stop offset="45%" class="ornament-stop-ochre"/>
          <stop offset="75%" class="ornament-stop-silver"/>
          <stop offset="100%" class="ornament-stop-shadow"/>
        </radialGradient>
      </defs>
      <rect role="img" aria-label="Baroque acanthus scroll ornament in antique silver and ochre" x="77" y="42" width="352" height="74" rx="37" fill="url(#ornament-tone)"/>
      <text class="brand-name" x="254" y="175" text-anchor="middle" textLength="300" lengthAdjust="spacingAndGlyphs">Sorrina by Velk</text>
      <rect role="img" aria-label="Baroque acanthus scroll ornament in antique silver and ochre" x="77" y="196" width="352" height="74" rx="37" fill="url(#ornament-tone)"/>
    </svg>
  </section>

  <section class="card card--back">
    <svg class="card__art" viewBox="0 0 509 310" xmlns="http://www.w3.org/2000/svg">
      <defs>
        <radialGradient id="crest-tone" cx="50%" cy="45%" r="60%">
          <stop offset="0%" class="ornament-stop-highlight"/>
          <stop offset="45%" class="ornament-stop-ochre"/>
          <stop offset="75%" class="ornament-stop-silver"/>
          <stop offset="100%" class="ornament-stop-shadow"/>
        </radialGradient>
      </defs>
      <rect role="img" aria-label="Baroque acanthus crest ornament in antique silver and ochre" x="55" y="80" width="278" height="54" rx="27" fill="url(#crest-tone)"/>
      <text class="contact__title" x="57" y="183" textLength="278" lengthAdjust="spacingAndGlyphs">Marianne Velk - Fashion Designer</text>
      <text class="contact__line" x="57" y="213">P: 04 0163 5271</text>
      <text class="contact__line" x="57" y="241">E: sorrinabyvelk@mailbrook.net</text>
      <text class="contact__line" x="57" y="270">W: www.threadpage.net/SOrrinaByVelk</text>
    </svg>
  </section>
</main>
</body>
</html>
```